Makers' Hollow - Landing page for small and large screen

Makers’ Hollow gives you the space you need to take your side project from idea to reality.

With three days of focused work, it’s a place for you iron out the details of your business idea away from the distractions of the city.

The full copy and structure is here:
https://www.makershollow.example.co.uk/landing

What it needs, a touch of colour.

Target Market(s)

25-35 working in digital industry, software developer, a UI or UX designer

Number of Pages Required

1 page

Font styles to use
Sans Serif

Colors
0292cd
33b8a4
86cfc6
fdf9cf
ec1f27

Requirements
Should not have
• gradients or too much images

```html
<!DOCTYPE html>
<html lang="en">
<head>
<meta charset="utf-8">
<title>Makers' Hollow – Landing</title>
<link href="https://fonts.googleapis.com/css2?family=Nunito+Sans:wght@400;600;700;800&display=swap" rel="stylesheet">
<style>
:root{
  --blue:#0292cd;
  --teal:#33b8a4;
  --mint:#86cfc6;
  --cream:#fdf9cf;
  --red:#ec1f27;
  --ink:#2e2e2e;
  --body:#6b6b6b;
  --mist:#f2f2f3;
  --line:#e2e2e2;
  --dark:#262626;
  --white:#ffffff;
}
*{box-sizing:border-box;margin:0;padding:0}
html,body{width:1200px;height:2496px;overflow:hidden}
body{position:relative;background:var(--white);font-family:"Nunito Sans",sans-serif;color:var(--body)}
.block{position:absolute;left:0;width:1200px}
p{font-size:15px;line-height:1.6}

.site-header{top:0;height:160px;background:var(--blue);display:flex;flex-direction:column;align-items:center;justify-content:center;color:var(--white)}
.brand-mark{width:44px;height:44px;border-radius:50%;border:3px solid var(--white);margin-bottom:8px}
.brand-name{font-size:22px;font-weight:800;letter-spacing:3px;text-transform:uppercase}
.brand-tagline{margin-top:4px;font-size:12px;letter-spacing:1px;opacity:.85}

.intro{top:160px;height:480px}
.intro-copy{position:absolute;left:90px;top:80px;width:640px}
.intro-lead{font-size:19px;line-height:1.5;color:var(--ink);font-weight:600;margin-bottom:22px}
.intro-lead strong{color:var(--blue)}
.intro-copy p{margin-bottom:14px}
.intro-photo{position:absolute;left:792px;top:0;width:320px;height:460px;background:linear-gradient(160deg,#eef0f2,#c9ccd0)}

.focus{top:650px;height:270px;background:var(--mist);text-align:center}
.focus h2{position:absolute;left:250px;width:700px;top:36px;font-size:22px;line-height:1.45;color:var(--ink);font-weight:700}
.focus-copy{position:absolute;left:200px;width:800px;top:126px}
.focus-copy p{font-size:14px;margin-bottom:12px}
.focus-copy b{color:var(--ink)}

.benefits{top:920px;height:460px}
.benefits-photo{position:absolute;left:88px;top:8px;width:472px;height:432px;background:linear-gradient(150deg,#e9e1d6,#b9ad9e)}
.benefits-list{position:absolute;left:620px;top:100px;width:480px}
.benefits-list h3{font-size:20px;color:var(--ink);font-weight:700;margin-bottom:18px}
.benefits-list ul{list-style:none}
.benefits-list li{display:flex;align-items:center;gap:12px;font-size:15px;margin-bottom:11px}
.benefits-list svg{flex:none}

.stay{top:1380px;height:220px;background:var(--teal);text-align:center;color:var(--white)}
.stay h2{margin-top:52px;font-size:26px;font-weight:700}
.stay p{width:800px;margin:20px auto 0;font-size:14px;opacity:.95}

.organisers{top:1600px;height:640px}
.organisers h2{position:absolute;top:56px;width:100%;text-align:center;font-size:32px;color:var(--ink);font-weight:700}
.organiser-card{position:absolute;top:160px;width:500px;height:400px;border:1px solid var(--line);padding:40px 40px}
.organiser-card.first{left:90px}
.organiser-card.second{left:610px}
.avatar{width:84px;height:84px;border-radius:50%;margin-bottom:20px}
.avatar.rob{background:linear-gradient(160deg,#8aa0ad,#3e4b55)}
.avatar.ana{background:linear-gradient(160deg,#d9c9a3,#7d6a44)}
.organiser-name{font-size:15px;font-weight:800;letter-spacing:1.5px;color:var(--blue);text-transform:uppercase;margin-bottom:12px}
.organiser-card p{font-size:14px}
.social{display:flex;gap:10px;margin-top:22px}
.social span{width:26px;height:26px;border-radius:50%;background:var(--line)}
.social span.on{background:var(--blue)}

.feedback{top:2260px;left:90px;width:1020px;height:150px;background:var(--blue);color:var(--white);padding:34px 50px}
.feedback h2{font-size:24px;font-weight:700;margin-bottom:10px}
.feedback p{width:560px;font-size:14px;opacity:.95}
.feedback-button{position:absolute;right:50px;top:52px;background:var(--dark);color:var(--white);font-size:12px;font-weight:800;letter-spacing:1.5px;padding:14px 28px;border-radius:24px;text-transform:uppercase}

.site-footer{top:2440px;height:56px;text-align:center}
.site-footer p{font-size:12px}
.site-footer b{color:var(--blue)}
</style>
</head>
<body>

<header class="block site-header">
  <div class="brand-mark"></div>
  <div class="brand-name">Makers' Hollow</div>
  <div class="brand-tagline">Create. Connect. Collaborate.</div>
</header>

<section class="block intro">
  <div class="intro-copy">
    <p class="intro-lead"><strong>Makers’ Hollow</strong> gives you the space you need to take your side project from idea to reality.</p>
    <p>Sitting on a side project? Whether you’re a software developer, a UI or UX designer, a product creator or an eager maker, you’ll know how hard it is to find real, uninterrupted time for it while you hold down the day job.</p>
    <p>Phones buzzing, friends pinging, chat notifications, meetings, distractions are everywhere – and they do nothing for your motivation.</p>
    <p>So, if you have a seed of a business idea and need to nurture some focus, Makers’ Hollow is for you. Our three days of calm are built to push you forward, so you can get ready – and shipping – to go.</p>
  </div>
  <div class="intro-photo" role="img" aria-label="Photo of a person working on a laptop at a bright desk"></div>
</section>

<section class="block focus">
  <h2>With three days of focused work, it’s a place for you iron out the details of your business idea away from the distractions of the city.</h2>
  <div class="focus-copy">
    <p>Whatever stage your side project is at, we’re here to help it thrive. Our warm and friendly retreat is set up so you can <b>create, connect and collaborate</b> with like-minded folks. Fast wifi, quiet rooms, healthy meals and lots of coffee keep the momentum flowing.</p>
    <p>And while you’re busy getting your side project off the ground, we’ll take care of everything else so that you don’t have to worry about a thing. We’ll even make sure you have a steady supply of healthy, home-made snacks to keep you going.</p>
  </div>
</section>

<section class="block benefits">
  <div class="benefits-photo" role="img" aria-label="Photo of a cheerful group of friends celebrating in a bright living room"></div>
  <div class="benefits-list">
    <h3>Join the Retreat and enjoy:</h3>
    <ul>
      <li><svg width="18" height="18" viewBox="0 0 18 18"><circle cx="9" cy="9" r="9" fill="#33b8a4"/><path d="M5 9.3l2.6 2.6L13 6.5" fill="none" stroke="#fff" stroke-width="2"/></svg>Three, full days of distraction free work</li>
      <li><svg width="18" height="18" viewBox="0 0 18 18"><circle cx="9" cy="9" r="9" fill="#33b8a4"/><path d="M5 9.3l2.6 2.6L13 6.5" fill="none" stroke="#fff" stroke-width="2"/></svg>A chance to hone your side project away from the office</li>
      <li><svg width="18" height="18" viewBox="0 0 18 18"><circle cx="9" cy="9" r="9" fill="#33b8a4"/><path d="M5 9.3l2.6 2.6L13 6.5" fill="none" stroke="#fff" stroke-width="2"/></svg>The opportunity to collaborate with likeminded creatives</li>
      <li><svg width="18" height="18" viewBox="0 0 18 18"><circle cx="9" cy="9" r="9" fill="#33b8a4"/><path d="M5 9.3l2.6 2.6L13 6.5" fill="none" stroke="#fff" stroke-width="2"/></svg>Good, honest feedback and insight from fellow attendees</li>
      <li><svg width="18" height="18" viewBox="0 0 18 18"><circle cx="9" cy="9" r="9" fill="#33b8a4"/><path d="M5 9.3l2.6 2.6L13 6.5" fill="none" stroke="#fff" stroke-width="2"/></svg>Daily yoga and meditation to help fuel your ideas</li>
      <li><svg width="18" height="18" viewBox="0 0 18 18"><circle cx="9" cy="9" r="9" fill="#33b8a4"/><path d="M5 9.3l2.6 2.6L13 6.5" fill="none" stroke="#fff" stroke-width="2"/></svg>Three, nutritious and delicious meals a day</li>
      <li><svg width="18" height="18" viewBox="0 0 18 18"><circle cx="9" cy="9" r="9" fill="#33b8a4"/><path d="M5 9.3l2.6 2.6L13 6.5" fill="none" stroke="#fff" stroke-width="2"/></svg>Healthy, low-sugar snacks to get you through the day</li>
    </ul>
  </div>
</section>

<section class="block stay">
  <h2>Where you’ll be staying</h2>
  <p>A retreat needn’t be a remote cabin in the woods. Our hollow is a restored farmhouse set in quiet green hills, just an hour from the city. Private rooms, shared workspaces and long walks all help to keep your mind on the work.</p>
</section>

<section class="block organisers">
  <h2>Meet Your Retreat Organisers</h2>
  <article class="organiser-card first">
    <div class="avatar rob" role="img" aria-label="Portrait photo of organiser Rob Calder"></div>
    <div class="organiser-name">Rob Calder</div>
    <p>A software engineer in Leeds, Rob knows only too well the challenges faced by creatives. It’s this that first inspired the retreat. With a background in start-ups, he loves helping people turn ideas into good apps.</p>
    <div class="social"><span></span><span class="on"></span><span></span></div>
  </article>
  <article class="organiser-card second">
    <div class="avatar ana" role="img" aria-label="Portrait photo of organiser Ana Marsh"></div>
    <div class="organiser-name">Ana Marsh</div>
    <p>An internationally certified yoga teacher, Ana loves connecting with people and discovering how she can help them get the best out of their day – and their work. During attendee days she’ll guide sessions to keep your energy flowing.</p>
    <div class="social"><span></span><span class="on"></span><span></span></div>
  </article>
</section>

<section class="block feedback">
  <h2>What do you think?</h2>
  <p>Second guess? Keen to know more? Share some feedback via the button below and we can have the retreat in no time.</p>
  <div class="feedback-button">Share your thoughts</div>
</section>

<footer class="block site-footer">
  <p>© 2019 <b>MAKERS' HOLLOW</b> All Right Reserved</p>
</footer>

</body>
</html>
```